Hi,

I would like to have a invitation made for a party. exactly like the picture in the link below.

http://pinboardia.example/pin/529174603381046725/

However, Please change the colors into fun/ girly feeling. font can be different and size of the card should be the same

Name of the girl: RUBA
What: Bachelorette Party
Where:TIKO Boat
Dubai Coral Sails Club
When:7th of February 2013

No RSVP required. (so no need to put it)

```html
<!DOCTYPE html>
<html lang="en">
<head>
<meta charset="utf-8">
<title>Ruba's Bachelorette Invitation</title>
<link rel="stylesheet" href="https://fonts.googleapis.com/css2?family=Kaushan+Script&family=Lato:wght@400;700&family=Rye&display=swap">
<style>
  :root {
    --paper: #ffffff;
    --ink: #111111;
    --fold-line: #3a3a3a;
    --lilac: #d5a3df;
    --lilac-soft: #ecd3f1;
    --lilac-frame: #dcb6e4;
  }
  html, body {
    margin: 0;
    padding: 0;
    width: 1200px;
    height: 787px;
    overflow: hidden;
    background: var(--paper);
  }
  .canvas {
    position: relative;
    width: 1200px;
    height: 787px;
    background: var(--paper);
    font-family: "Lato", "Gill Sans", sans-serif;
    color: var(--ink);
  }
  .card {
    position: absolute;
    left: 76px;
    top: 54px;
    width: 979px;
    height: 582px;
    border: 1.5px solid var(--fold-line);
    box-sizing: border-box;
  }
  .fold {
    position: absolute;
    top: 54px;
    width: 1.5px;
    height: 582px;
    background: var(--fold-line);
  }
  .fold--first { left: 401px; }
  .fold--second { left: 727px; }

  .border-band {
    position: absolute;
    left: 77px;
    width: 977px;
    height: 54px;
    background: linear-gradient(180deg, var(--lilac-soft) 0%, var(--lilac) 50%, var(--lilac-soft) 100%);
    opacity: 0.75;
    border-radius: 27px;
  }
  .border-band--top { top: 78px; }
  .border-band--bottom { top: 550px; }

  .flourish {
    position: absolute;
    background: radial-gradient(circle, var(--lilac) 0%, var(--lilac-soft) 100%);
    border-radius: 50%;
  }
  .flourish--dot-i { left: 203px; top: 348px; width: 44px; height: 30px; }
  .flourish--details { left: 864px; top: 158px; width: 56px; height: 50px; }

  .bride-name {
    position: absolute;
    left: 92px;
    top: 150px;
    margin: 0;
    font-family: "Kaushan Script", cursive;
    font-weight: 400;
    font-size: 92px;
    line-height: 1;
  }
  .tagline {
    position: absolute;
    top: 283px;
    margin: 0;
    font-family: "Lato", sans-serif;
    font-weight: 400;
    font-size: 27px;
    letter-spacing: 0.5px;
    line-height: 1;
  }
  .tagline--left { left: 110px; }
  .tagline--right { left: 414px; }

  .headline {
    position: absolute;
    left: 90px;
    top: 400px;
    width: 640px;
    height: 150px;
  }
  .headline text {
    font-family: "Rye", serif;
    font-size: 150px;
    fill: var(--ink);
  }

  .details {
    position: absolute;
    left: 771px;
    top: 182px;
    width: 238px;
    height: 328px;
    box-sizing: border-box;
    border: 2px solid var(--lilac-frame);
    border-radius: 9px;
    text-align: center;
  }
  .details__title {
    margin: 52px 0 0;
    font-family: "Rye", serif;
    font-weight: 400;
    font-size: 25px;
    line-height: 1.05;
    color: var(--ink);
    text-shadow: 1px 1px 0 #777777;
  }
  .details__block {
    margin: 40px 0 0;
    font-size: 17px;
    line-height: 23px;
  }
  .details__block + .details__block { margin-top: 23px; }
</style>
</head>
<body>
<main class="canvas">
  <div class="card"></div>
  <div class="fold fold--first"></div>
  <div class="fold fold--second"></div>

  <div class="border-band border-band--top" role="img" aria-label="Lilac ornamental scroll border across the top of the card"></div>
  <div class="border-band border-band--bottom" role="img" aria-label="Lilac ornamental scroll border across the bottom of the card"></div>

  <h1 class="bride-name">Ruba's</h1>
  <p class="tagline tagline--left">LAST CHANCE TO</p>
  <p class="tagline tagline--right">CELEBRATE BEING</p>

  <div class="flourish flourish--dot-i" role="img" aria-label="Small lilac damask ornament dotting the letter I"></div>
  <svg class="headline" viewBox="0 0 640 150" aria-label="SINGLE">
    <text x="2" y="138" textLength="636" lengthAdjust="spacingAndGlyphs">SINGLE</text>
  </svg>

  <section class="details">
    <div class="flourish flourish--details" style="left:91px;top:-26px;" role="img" aria-label="Small lilac damask ornament crowning the details frame"></div>
    <h2 class="details__title">YOUR<br>INVITED</h2>
    <p class="details__block">Where:<br>TIKO Boat<br>Dubai Coral Sails Club</p>
    <p class="details__block">When:<br>7th of February 2013</p>
  </section>
</main>
</body>
</html>
```